Window Perf design with eadership quotes

I am wanting to create a window perf that covers windows in a conference room. I have included a picture of the windows. Each window is 26 1/2 inches by 92 inches. I have also included several other pictures to give an example of how I would like the Quotes to look.

Some Quotes I would like to use
1. Your Future is created by what you do today not tomorrow.
2. The answer is Yes
3. People don't care how much you know until they know how much you care.
4. Treat employees like they make a difference and they will.
5. Don't follow the crowd, Let the crowd follow you.
6. Treat people as if they were what they ought to be , and help them become what they are capable of being.
7. Leadership is not a title, its a behavior. LIVE IT
8. We make a living by what we get, We make a life by what we give.
9. Success is not final, failure is not fatal: it is courage to continue that counts.
10. The best way to predict your future is to create it.
11. The supreme quality of leadership is Integrity.
12. Whatever you are, Be a good one

Quotes

• I am imore interested in how this looks rather than including all of the quotes. I also ant this to be a solid background design for privacy.

```html
<!DOCTYPE html>
<html lang="en">
<head>
<meta charset="utf-8">
<title>Leadership Quotes – Window Perf Banners</title>
<link href="https://fonts.googleapis.com/css2?family=Bebas+Neue&display=swap" rel="stylesheet">
<style>
  :root {
    --ink: #0c0c0c;
    --paper: #ffffff;
    --accent-red: #e41f26;
    --field-red: #f0412c;
    --field-red-deep: #e2321f;
    --quote-white: #ffffff;
    --quote-grey: #b9b9b9;
  }
  html, body {
    margin: 0;
    padding: 0;
    overflow: hidden;
    background: var(--paper);
  }
  .canvas {
    position: relative;
    width: 1200px;
    height: 900px;
    background: var(--paper);
    overflow: hidden;
    font-family: "Bebas Neue", "Oswald", Impact, sans-serif;
  }
  .banner {
    position: absolute;
    top: 44px;
    width: 232px;
    height: 806px;
  }
  .banner--living  { left: 98px; }
  .banner--success { left: 356px; }
  .banner--treat   { left: 612px; }
  .banner--care    { left: 866px; }

  .banner__backdrop {
    position: absolute;
    inset: 0;
    width: 100%;
    height: 100%;
    display: block;
  }
  .quote {
    position: absolute;
    top: 26px;
    left: 16px;
    right: 14px;
    margin: 0;
    color: var(--quote-white);
    text-transform: uppercase;
    line-height: 0.86;
    letter-spacing: 0.2px;
  }
  .quote__line {
    display: flex;
    align-items: center;
    gap: 5px;
    white-space: nowrap;
  }
  .is-white { color: var(--quote-white); }
  .is-grey  { color: var(--quote-grey); }
  .is-red   { color: var(--accent-red); }

  .stack {
    display: inline-flex;
    flex-direction: column;
    justify-content: center;
    line-height: 0.9;
  }
</style>
</head>
<body>
<main class="canvas">

  <!-- Banner 1 -->
  <section class="banner banner--living">
    <svg class="banner__backdrop" viewBox="0 0 232 806" preserveAspectRatio="none" aria-hidden="true">
      <rect width="232" height="806" fill="var(--field-red)"/>
      <polygon points="0,0 232,0 232,504 0,560" fill="var(--ink)"/>
      <polygon points="0,560 232,504 232,520 0,578" fill="var(--paper)"/>
    </svg>
    <rect role="img" aria-label="Red field with faint repeated lettering texture for privacy"></rect>
    <p class="quote">
      <span class="quote__line" style="font-size:46px">We make a</span>
      <span class="quote__line is-red" style="font-size:84px">Living</span>
      <span class="quote__line" style="font-size:52px">By what</span>
      <span class="quote__line">
        <span class="stack is-grey" style="font-size:17px"><span>We</span><span>get</span></span>
        <span style="font-size:50px">We make</span>
      </span>
      <span class="quote__line is-red" style="font-size:76px">A life</span>
      <span class="quote__line" style="font-size:44px">By what we</span>
      <span class="quote__line is-grey" style="font-size:104px">Give</span>
    </p>
  </section>

  <!-- Banner 2 -->
  <section class="banner banner--success">
    <svg class="banner__backdrop" viewBox="0 0 232 806" preserveAspectRatio="none" role="img" aria-label="Red field with faint repeated lettering texture for privacy">
      <rect width="232" height="806" fill="var(--field-red)"/>
      <polygon points="0,0 232,0 232,436 0,496" fill="var(--ink)"/>
      <polygon points="0,496 232,436 232,452 0,514" fill="var(--paper)"/>
    </svg>
    <p class="quote">
      <span class="quote__line is-red" style="font-size:62px">Success</span>
      <span class="quote__line">
        <span style="font-size:50px">Is</span>
        <span class="stack" style="font-size:13px"><span>Not</span></span>
        <span class="is-grey" style="font-size:64px">Final</span>
      </span>
      <span class="quote__line is-red" style="font-size:66px">Failure</span>
      <span class="quote__line">
        <span style="font-size:50px">Is</span>
        <span class="stack" style="font-size:13px"><span>Not</span></span>
        <span class="is-grey" style="font-size:64px">Fatal</span>
      </span>
      <span class="quote__line">
        <span class="stack" style="font-size:19px"><span>It</span><span>is</span></span>
        <span class="is-red" style="font-size:50px">Courage</span>
      </span>
      <span class="quote__line" style="font-size:30px">To continue that</span>
      <span class="quote__line is-grey" style="font-size:72px">Counts</span>
    </p>
  </section>

  <!-- Banner 3 -->
  <section class="banner banner--treat">
    <svg class="banner__backdrop" viewBox="0 0 232 806" preserveAspectRatio="none" role="img" aria-label="Red field with faint repeated lettering texture for privacy">
      <rect width="232" height="806" fill="var(--field-red)"/>
      <polygon points="0,0 232,0 232,376 0,436" fill="var(--ink)"/>
      <polygon points="0,436 232,376 232,392 0,454" fill="var(--paper)"/>
    </svg>
    <p class="quote">
      <span class="quote__line" style="font-size:72px">Treat</span>
      <span class="quote__line is-red" style="font-size:68px">People</span>
      <span class="quote__line">
        <span class="stack" style="font-size:13px"><span>As</span><span>if</span></span>
        <span class="is-grey" style="font-size:44px">They were</span>
      </span>
      <span class="quote__line">
        <span class="stack" style="font-size:13px"><span>What</span><span>they</span></span>
        <span class="is-grey" style="font-size:36px">Ought to be</span>
      </span>
      <span class="quote__line is-red" style="font-size:46px">Help them</span>
      <span class="quote__line">
        <span class="stack" style="font-size:13px"><span>Become</span><span>what</span></span>
        <span class="is-grey" style="font-size:38px">They</span>
        <span style="font-size:38px">are</span>
      </span>
      <span class="quote__line" style="font-size:27px">Capable of being</span>
    </p>
  </section>

  <!-- Banner 4 -->
  <section class="banner banner--care">
    <svg class="banner__backdrop" viewBox="0 0 232 806" preserveAspectRatio="none" role="img" aria-label="Red field with faint repeated lettering texture for privacy">
      <rect width="232" height="806" fill="var(--field-red)"/>
      <polygon points="0,0 232,0 232,324 0,382" fill="var(--ink)"/>
      <polygon points="0,382 232,324 232,340 0,400" fill="var(--paper)"/>
    </svg>
    <p class="quote">
      <span class="quote__line" style="font-size:70px">People</span>
      <span class="quote__line">
        <span class="stack is-red" style="font-size:13px"><span>Don't</span><span>care</span></span>
        <span class="is-grey" style="font-size:42px">How much</span>
      </span>
      <span class="quote__line is-grey" style="font-size:50px">You know</span>
      <span class="quote__line">
        <span class="stack" style="font-size:18px"><span>Until</span><span>they</span></span>
        <span class="is-grey" style="font-size:56px">Know</span>
      </span>
      <span class="quote__line">
        <span class="stack" style="font-size:13px"><span>How</span><span>much</span></span>
        <span class="is-red" style="font-size:44px">You care</span>
      </span>
    </p>
  </section>

</main>
</body>
</html>
```